Kestrim LLC, needs a web page no more than 5 pages (for now)

Kestrim is a general contractor. Our services include general contracting, design-build construction, disaster recovery and environmental remediation. Our main clients are KZE, HJ, State and Local Gov't Agencies, Hospitals and Schools. Kestrim is also a SDVOSB.

```html
<!DOCTYPE html>
<html lang="en">
<head>
<meta charset="utf-8">
<title>Kestrim LLC — General Contractor</title>
<link href="https://fonts.googleapis.com/css2?family=Poppins:ital,wght@0,400;0,500;0,600;0,700;1,400&display=swap" rel="stylesheet">
<style>
:root{
  --gold:#c9a227;
  --gold-light:#e6c45a;
  --gold-dark:#8f6b12;
  --ink:#1e1e1e;
  --text:#3d3d3d;
  --muted:#8a8a8a;
  --line:#e3e3e3;
  --btn-dark:#3a3a3a;
  --white:#ffffff;
}
*{margin:0;padding:0;box-sizing:border-box}
html,body{width:1200px;height:5038px;overflow:hidden}
body{position:relative;background:var(--white);font-family:'Poppins',sans-serif;color:var(--text)}
.abs{position:absolute}
.gold-btn{position:absolute;display:flex;align-items:center;justify-content:center;background:linear-gradient(90deg,var(--gold-dark),var(--gold-light) 55%,var(--gold-dark));color:var(--ink);font-weight:600;font-size:15px;text-transform:uppercase}
.dark-btn{position:absolute;display:flex;align-items:center;justify-content:center;background:var(--btn-dark);color:var(--white);font-size:11px;font-weight:600;border-radius:3px}
.photo{position:absolute}
.brand{font-family:'Poppins',sans-serif;font-weight:600;color:var(--gold-dark);letter-spacing:2px}
.arc{position:absolute}

/* header */
.header{position:absolute;left:0;top:0;width:1200px;height:122px;background:var(--white);z-index:3}
.header .brand{position:absolute;left:70px;top:40px;font-size:32px;line-height:48px}
.nav{position:absolute;left:414px;top:50px;display:flex;gap:18px;font-size:13px;color:var(--ink);text-transform:uppercase}
.nav a{color:inherit;text-decoration:none}
.nav .active{font-weight:600}
.callbox{position:absolute;left:800px;top:0;width:400px;height:127px;background:linear-gradient(100deg,var(--gold-dark),var(--gold-light) 50%,var(--gold));clip-path:polygon(0 0,100% 0,100% 100%,55px 100%);z-index:4}
.callbox .label{position:absolute;left:140px;top:32px;font-size:15px;font-weight:500;color:var(--ink)}
.callbox .num{position:absolute;left:90px;top:66px;font-size:33px;line-height:1.2;color:var(--ink)}
.callbox svg{position:absolute;left:90px;top:24px}

/* hero */
.hero{position:absolute;left:0;top:122px;width:1200px;height:748px}
.hero .photo{left:0;top:0;width:1200px;height:748px;background:linear-gradient(90deg,#efedeb 0%,#e4e0dc 40%,#c9c0b5 70%,#8f7f6c 100%);clip-path:polygon(0 0,100% 0,100% 640px,50% 735px,0 640px)}
.hero .chev{position:absolute;left:0;top:0}
.hero .eyebrow{position:absolute;left:72px;top:183px;font-size:15px;font-weight:500;line-height:20px;color:var(--ink)}
.hero h1{position:absolute;left:68px;top:208px;font-size:84px;line-height:84px;font-weight:600;color:var(--ink);letter-spacing:1px}
.hero p{position:absolute;left:72px;top:300px;width:470px;font-size:14px;line-height:24px;color:var(--ink)}

/* section titles */
.sec-title{position:absolute;font-size:40px;font-weight:600;color:var(--ink);text-transform:uppercase;line-height:1}
.sec-title.center{left:0;width:1200px;text-align:center}
.deco{position:absolute}

/* about */
.about-frame{position:absolute;left:148px;top:1023px;width:402px;height:478px;border:1.5px solid var(--white)}
.about-sub{position:absolute;left:621px;top:1128px;width:454px;font-size:20px;font-weight:600;line-height:31px;color:var(--ink);text-align:justify}
.about-text{position:absolute;left:621px;top:1203px;width:454px;font-size:14px;line-height:26.5px;color:var(--text);text-align:justify}

/* services */
.card{position:absolute;top:1802px;width:346px;height:466px;background:var(--white);box-shadow:0 2px 14px rgba(0,0,0,.13)}
.card .photo{left:18px;top:18px;width:310px;height:227px}
.card h3{position:absolute;left:0;top:273px;width:100%;text-align:center;font-size:16.5px;font-weight:600;color:var(--ink)}
.card p{position:absolute;left:22px;top:305px;width:302px;text-align:center;font-size:11px;line-height:19px;color:var(--text)}
.card .dark-btn{left:112px;top:395px;width:122px;height:46px}

/* testimonials */
.quote-box{position:absolute;top:2702px;width:464px;height:221px;border:2px solid var(--line);border-radius:24px;background:var(--white)}
.quote-box .stars{position:absolute;right:34px;top:40px;font-size:17px;color:var(--gold);letter-spacing:1px}
.quote-box .stars .off{color:#555}
.quote-box p{position:absolute;left:36px;top:84px;width:404px;font-size:12.5px;font-style:italic;line-height:21px;color:var(--text)}
.qmark{position:absolute;top:2660px;font-size:110px;font-weight:700;line-height:1;color:var(--gold);font-family:Georgia,serif}
.avatar{position:absolute;top:2948px;width:68px;height:68px;border-radius:50%;background:linear-gradient(160deg,#c7c2bb,#5d5348);border:2px solid var(--white);box-shadow:0 0 0 1px var(--line)}
.who{position:absolute;top:2962px;font-size:13px;font-weight:600;color:var(--ink)}
.who span{display:block;font-size:11px;font-weight:400;color:var(--text)}
.dots{position:absolute;left:565px;top:3068px;display:flex;gap:5px}
.dots i{width:9px;height:9px;border-radius:50%;border:1px solid #555}
.dots i.on{background:#444}

/* banner */
.banner{position:absolute;left:0;top:3159px;width:1200px;height:495px;background:linear-gradient(90deg,#a38a6a 0%,#cfc3b4 30%,#ebe7e3 55%,#f1efed 100%)}
.banner h2{position:absolute;left:514px;top:152px;font-size:50px;line-height:60px;font-weight:600;letter-spacing:2px;color:#4b4b4b;white-space:nowrap}
.banner p{position:absolute;left:560px;top:226px;width:540px;text-align:center;font-size:14px;line-height:24px;color:var(--ink)}

/* contact */
.field{position:absolute;height:46px;background:var(--white);border:1px solid #e8e8e8;box-shadow:0 1px 6px rgba(0,0,0,.08);font-size:13px;color:#aaa;padding:14px 18px}
.contact-frame{position:absolute;left:666px;top:3802px;width:402px;height:478px;border:1.5px solid var(--white)}

/* footer */
.footer{position:absolute;left:0;top:4470px;width:1200px;height:568px}
.footer .bg{position:absolute;left:0;top:0;width:1200px;height:568px;background:linear-gradient(180deg,#f4f4f4,#ebebeb);clip-path:polygon(0 110px,50% 0,100% 110px,100% 100%,0 100%)}
.footer .brand{position:absolute;left:192px;top:262px;font-size:32px;line-height:48px}
.social{position:absolute;top:362px;width:36px;height:36px;border-radius:50%;background:linear-gradient(135deg,var(--gold-light),var(--gold-dark))}
.foot-h{position:absolute;top:218px;font-size:23px;font-weight:600;color:var(--ink)}
.links{position:absolute;left:552px;top:286px;list-style:none;font-size:13.5px;color:var(--ink)}
.links li{height:33px;position:relative;padding-left:20px}
.links li::before{content:"";position:absolute;left:0;top:7px;width:7px;height:7px;border-radius:50%;background:var(--gold)}
.cinfo{position:absolute;left:823px;font-size:13.5px;line-height:22px;color:var(--ink)}
.cinfo .ic{position:absolute;left:0;top:0;width:36px;height:36px;border-radius:50%;background:linear-gradient(135deg,var(--gold-light),var(--gold-dark))}
.cinfo .ic svg{position:absolute;left:9px;top:9px}
.cinfo .tx{position:absolute;left:50px;top:-4px;width:200px}
.footer .rule{position:absolute;left:68px;top:482px;width:1064px;height:1px;background:#cfcfcf}
.footer .copy{position:absolute;left:0;top:512px;width:1200px;text-align:center;font-size:14px;color:var(--ink)}
</style>
</head>
<body>

<header class="header">
  <div class="brand">KESTRIM</div>
  <nav class="nav">
    <a class="active" href="#">Home</a><a href="#">About Us</a><a href="#">Services</a><a href="#">Clients</a><a href="#">Contact Us</a>
  </nav>
</header>
<div class="callbox">
  <svg width="38" height="38" viewBox="0 0 38 38"><circle cx="19" cy="19" r="17" fill="none" stroke="#1e1e1e" stroke-width="2"/><path d="M13 11c1-1 2-1 3 0l2 3c0 1 0 2-1 2l-1 1c1 2 3 4 5 5l1-1c1-1 2-1 2-1l3 2c1 1 1 2 0 3l-1 1c-5 1-13-7-12-12z" fill="#1e1e1e"/></svg>
  <div class="label">CONTACT US TODAY !</div>
  <div class="num">(555) 014-2287</div>
</div>

<section class="hero">
  <div class="photo" role="img" aria-label="Photo of a site engineer in a hard hat and safety vest holding plans beside a manager in a suit, with houses under construction behind them"></div>
  <svg class="chev" width="1200" height="748" viewBox="0 0 1200 748"><polygon points="0,640 600,735 1200,640 1200,655 600,748 0,655" fill="#c9a227"/><polygon points="0,640 600,735 600,748 0,655" fill="#e0bd50"/></svg>
  <div class="eyebrow">WELCOME TO</div>
  <h1>KESTRIM</h1>
  <p>General contracting, design-build construction, disaster recovery and environmental remediation for public agencies.</p>
  <div class="gold-btn" style="left:70px;top:363px;width:174px;height:50px;">Contact Us</div>
</section>

<section>
  <div class="photo" style="left:125px;top:997px;width:448px;height:532px;background:linear-gradient(160deg,#d8d4cf,#a39481 55%,#6e604f)" role="img" aria-label="Photo of two builders in hard hats reviewing a blueprint on a building site"></div>
  <div class="about-frame"></div>
  <svg class="arc" style="left:616px;top:1020px" width="64" height="36" viewBox="0 0 64 36"><path d="M5 33 A28 28 0 0 1 50 9" fill="none" stroke="#c9a227" stroke-width="4" stroke-linecap="round"/></svg>
  <h2 class="sec-title" style="left:621px;top:1048px;">About Us</h2>
  <svg class="deco" style="left:621px;top:1094px" width="90" height="10"><line x1="0" y1="5" x2="84" y2="5" stroke="#c9a227" stroke-width="3"/><circle cx="84" cy="5" r="4" fill="#c9a227"/></svg>
  <div class="about-sub">Lorem ipsum dolor sit amet, consectetur adipiscing elit,</div>
  <div class="about-text">sed do eiusmod tempor incididunt ut labore et dolore magna aliqua. Ut enim ad minim veniam, quis nostrud exercitation ullamco laboris nisi ut aliquip ex ea commodo consequat. Duis aute irure dolor in reprehenderit in voluptate velit esse cillum dolore eu fugiat nulla pariatur. Excepteur sint occaecat cupidatat non proident, sunt in culpa qui officia deserunt mollit anim id est laborum.</div>
  <div class="gold-btn" style="left:621px;top:1395px;width:174px;height:52px;">Contact Us</div>
</section>

<section>
  <svg class="arc" style="left:448px;top:1656px" width="64" height="36" viewBox="0 0 64 36"><path d="M5 33 A28 28 0 0 1 50 9" fill="none" stroke="#c9a227" stroke-width="4" stroke-linecap="round"/></svg>
  <h2 class="sec-title center" style="top:1684px;">Our Services</h2>
  <svg class="deco" style="left:555px;top:1730px" width="92" height="10"><line x1="4" y1="5" x2="88" y2="5" stroke="#c9a227" stroke-width="3"/><circle cx="4" cy="5" r="4" fill="#c9a227"/><circle cx="88" cy="5" r="4" fill="#c9a227"/></svg>

  <article class="card" style="left:68px;">
    <div class="photo" style="background:linear-gradient(170deg,#dcdad6,#b89a6c 60%,#6b5d4a)" role="img" aria-label="Photo of a contracting team in hard hats gathered around plans on a table"></div>
    <h3>GENERAL CONTRACTING</h3>
    <p>Lorem ipsum dolor sit amet, consectetur adipiscing elit, sed do eiusmod tempor incididunt ut labore et dolore magna aliqua. Quis ipsum suspendisse ultrices gravida. Risus commodo viverra maecenas ...</p>
    <div class="dark-btn">READ MORE</div>
  </article>
  <article class="card" style="left:430px;">
    <div class="photo" style="background:linear-gradient(160deg,#3a3a3c,#e9e9e9 45%,#d4d4d4)" role="img" aria-label="Photo of hands drafting architectural plans with a pen and ruler"></div>
    <h3>DESIGN-BUILD CONSTRUCTION</h3>
    <p>Lorem ipsum dolor sit amet, consectetur adipiscing elit, sed do eiusmod tempor incididunt ut labore et dolore magna aliqua. Quis ipsum suspendisse ultrices gravida. Risus commodo viverra maecenas ...</p>
    <div class="dark-btn">READ MORE</div>
  </article>
  <article class="card" style="left:790px;">
    <div class="photo" style="background:linear-gradient(140deg,#6f7445,#4e5038 50%,#8a8f62)" role="img" aria-label="Aerial photo of flood damage along a railway line"></div>
    <h3>DISASTER RECOVERY</h3>
    <p>Lorem ipsum dolor sit amet, consectetur adipiscing elit, sed do eiusmod tempor incididunt ut labore et dolore magna aliqua. Quis ipsum suspendisse ultrices gravida. Risus commodo viverra maecenas ...</p>
    <div class="dark-btn">READ MORE</div>
  </article>

  <div class="gold-btn" style="left:500px;top:2318px;width:200px;height:51px;font-size:12px;">View All Services</div>
</section>

<section>
  <svg class="arc" style="left:398px;top:2502px" width="64" height="36" viewBox="0 0 64 36"><path d="M5 33 A28 28 0 0 1 50 9" fill="none" stroke="#c9a227" stroke-width="4" stroke-linecap="round"/></svg>
  <h2 class="sec-title center" style="top:2530px;">Our Testimonials</h2>
  <svg class="deco" style="left:553px;top:2576px" width="92" height="10"><line x1="4" y1="5" x2="88" y2="5" stroke="#c9a227" stroke-width="3"/><circle cx="4" cy="5" r="4" fill="#c9a227"/><circle cx="88" cy="5" r="4" fill="#c9a227"/></svg>

  <div class="quote-box" style="left:115px;">
    <div class="stars">★★★★<span class="off">★</span></div>
    <p>Lorem ipsum dolor sit amet, consectetur adipiscing elit, sed do eiusmod tempor incididunt ut labore et dolore magna aliqua. Ut enim ad minim veniam, quis nostrud exercitation ullamco laboris nisi ut aliquip ex ea commodo consequat.</p>
  </div>
  <div class="quote-box" style="left:625px;">
    <div class="stars">★★★★<span class="off">★</span></div>
    <p>Lorem ipsum dolor sit amet, consectetur adipiscing elit, sed do eiusmod tempor incididunt ut labore et dolore magna aliqua. Ut enim ad minim veniam, quis nostrud exercitation ullamco laboris nisi ut aliquip ex ea commodo consequat. Duis aute irure dolor in reprehenderit in voluptate velit.</p>
  </div>
  <svg class="deco" style="left:170px;top:2920px" width="40" height="24"><polygon points="0,0 36,0 20,20" fill="#fff" stroke="#e3e3e3" stroke-width="2"/><rect x="0" y="0" width="38" height="3" fill="#fff"/></svg>
  <svg class="deco" style="left:680px;top:2920px" width="40" height="24"><polygon points="0,0 36,0 20,20" fill="#fff" stroke="#e3e3e3" stroke-width="2"/><rect x="0" y="0" width="38" height="3" fill="#fff"/></svg>
  <div class="qmark" style="left:176px;">&ldquo;</div>
  <div class="qmark" style="left:686px;">&ldquo;</div>
  <div class="avatar" style="left:224px;" role="img" aria-label="Portrait photo of Marcus Dell"></div>
  <div class="who" style="left:306px;">MARCUS DELL<span>Lorem ipsum</span></div>
  <div class="avatar" style="left:731px;" role="img" aria-label="Portrait photo of Owen Hale"></div>
  <div class="who" style="left:815px;">OWEN HALE<span>Lorem ipsum</span></div>
  <div class="dots"><i class="on"></i><i></i><i></i><i></i></div>
</section>

<section class="banner" role="img" aria-label="Photo of a site engineer and a manager in hard hats pointing across a housing development">
  <h2>WE BUILD YOUR DREAM</h2>
  <p>Lorem ipsum dolor sit amet, consectetur adipiscing elit, sed do eiusmod tempor incididunt ut labore et dolore magna aliqua.</p>
  <div class="gold-btn" style="left:745px;top:293px;width:174px;height:51px;">Contact Us</div>
</section>

<section>
  <svg class="arc" style="left:118px;top:3810px" width="64" height="36" viewBox="0 0 64 36"><path d="M5 33 A28 28 0 0 1 50 9" fill="none" stroke="#c9a227" stroke-width="4" stroke-linecap="round"/></svg>
  <h2 class="sec-title" style="left:123px;top:3838px;">Contact Us</h2>
  <svg class="deco" style="left:123px;top:3884px" width="90" height="10"><line x1="0" y1="5" x2="84" y2="5" stroke="#c9a227" stroke-width="3"/><circle cx="84" cy="5" r="4" fill="#c9a227"/></svg>
  <div class="field" style="left:123px;top:3929px;width:217px;">First Name:</div>
  <div class="field" style="left:362px;top:3929px;width:219px;">Last Name:</div>
  <div class="field" style="left:123px;top:3994px;width:217px;">Phone:</div>
  <div class="field" style="left:362px;top:3994px;width:219px;">Email:</div>
  <div class="field" style="left:123px;top:4060px;width:458px;height:139px;padding-top:26px;">Mesage:</div>
  <div class="gold-btn" style="left:123px;top:4234px;width:172px;height:43px;font-size:13px;">Submit a Message</div>
  <div class="photo" style="left:643px;top:3779px;width:448px;height:532px;background:linear-gradient(160deg,#d9d6d2,#b39a78 55%,#73644f)" role="img" aria-label="Photo of two smiling builders in hard hats shaking hands on site"></div>
  <div class="contact-frame"></div>
</section>

<footer class="footer">
  <div class="bg" role="img" aria-label="Faint photo of construction workers behind the footer"></div>
  <svg class="abs" style="left:0;top:0" width="1200" height="125"><polygon points="0,110 600,0 1200,110 1200,118 600,14 0,118" fill="#c9a227"/></svg>
  <div class="brand">KESTRIM</div>
  <div class="social" style="left:208px;"></div>
  <div class="social" style="left:256px;"></div>
  <div class="social" style="left:304px;"></div>

  <div class="foot-h" style="left:549px;">LINKS</div>
  <svg class="abs" style="left:549px;top:256px" width="50" height="8"><line x1="0" y1="4" x2="44" y2="4" stroke="#c9a227" stroke-width="3"/><circle cx="44" cy="4" r="3.5" fill="#c9a227"/></svg>
  <ul class="links"><li>About Us</li><li>Services</li><li>Clients</li><li>Contact Us</li></ul>

  <div class="foot-h" style="left:821px;">CONTACT US</div>
  <svg class="abs" style="left:821px;top:256px" width="50" height="8"><line x1="0" y1="4" x2="44" y2="4" stroke="#c9a227" stroke-width="3"/><circle cx="44" cy="4" r="3.5" fill="#c9a227"/></svg>
  <div class="cinfo" style="top:290px;"><span class="ic"><svg width="18" height="18" viewBox="0 0 18 18"><path d="M9 1a6 6 0 0 1 6 6c0 4-6 10-6 10S3 11 3 7a6 6 0 0 1 6-6z" fill="#fff"/><circle cx="9" cy="7" r="2.2" fill="#b08a22"/></svg></span><span class="tx">Lorem ipsum,Lorem ipsum. Lorem ipsum</span></div>
  <div class="cinfo" style="top:346px;"><span class="ic"><svg width="18" height="18" viewBox="0 0 18 18"><path d="M4 2c1-1 2-1 3 0l2 3c0 1 0 1-1 2l-1 1c1 2 3 4 5 5l1-1c1-1 1-1 2-1l3 2c1 1 1 2 0 3l-1 1C10 18 0 8 2 4z" fill="#fff"/></svg></span><span class="tx" style="top:7px;">(555) 014-2287</span></div>
  <div class="cinfo" style="top:401px;"><span class="ic"><svg width="18" height="18" viewBox="0 0 18 18"><rect x="1" y="4" width="16" height="11" rx="1" fill="#fff"/><path d="M1 5l8 6 8-6" fill="none" stroke="#b08a22" stroke-width="1.5"/></svg></span><span class="tx" style="top:7px;">info@kestrimbuild.com</span></div>

  <div class="rule"></div>
  <div class="copy">Copyright © 2025 All Rights Reserved By Kestrim LLC</div>
</footer>

</body>
</html>
```